Webdesign für Baustoffhandel
Zielgruppe
Baustoffhandel - stationär sowie online
Aufgabenstellung
moder, witzig, evtl. Comic charakter, logo ist ähnlich dem Tauschwerk(Spiel) Männchen, farbig, Möglichkeit shop zu integrieren
siehe Logo bild

```html
<!DOCTYPE html>
<html lang="de">
<head>
<meta charset="utf-8">
<title>Steinmeister – Baustoffhandel</title>
<link href="https://fonts.googleapis.com/css2?family=Open+Sans:wght@400;600;700&display=swap" rel="stylesheet">
<style>
:root{
  --orange:#f6a54f;
  --orange-dark:#ef9535;
  --ink:#1b1b1b;
  --text:#3a3a3a;
  --grey-bar:#ececec;
  --footer:#f0f0f0;
  --green:#cde3c8;
  --red:#e3001b;
}
*{box-sizing:border-box;margin:0;padding:0}
html,body{width:1200px;height:3276px;overflow:hidden;background:var(--footer);font-family:"Open Sans",sans-serif;color:var(--text)}
.page{position:absolute;left:0;top:0;width:1200px;height:3276px;background:#fff;overflow:hidden}
.abs{position:absolute}
.topbar{left:0;top:0;width:1200px;height:25px;background:var(--grey-bar);font-size:11px;color:#444}
.topbar .item{position:absolute;top:5px;display:flex;align-items:center;gap:6px;white-space:nowrap}
.header{left:0;top:25px;width:1200px;height:111px;border-bottom:1px solid #ddd}
.brand{position:absolute;left:88px;top:66px;font-size:20px;font-weight:700;color:var(--ink);letter-spacing:.3px}
.nav a{position:absolute;top:69px;font-size:15px;font-weight:600;color:var(--ink);text-decoration:none;letter-spacing:.3px;white-space:nowrap}
.hero{left:0;top:136px;width:1200px;height:329px}
.hero-panel{position:absolute;left:0;top:0;width:519px;height:329px;background:var(--orange);text-align:center;color:#fff}
.hero-panel h1{position:absolute;left:0;width:519px;top:76px;font-size:21px;font-weight:700}
.hero-panel p{position:absolute;left:0;width:519px;top:124px;font-size:13px;line-height:17.5px}
.btn{position:absolute;background:var(--ink);color:#fff;font-size:14px;font-weight:700;display:flex;align-items:center;justify-content:center;letter-spacing:.3px;white-space:nowrap}
.hero-photo{position:absolute;left:519px;top:0;width:681px;height:329px;background:linear-gradient(160deg,#c9ccd2 0%,#d3413a 40%,#b52a27 65%,#5b6270 100%)}
h2{position:absolute;font-size:25px;font-weight:600;color:var(--ink)}
.rule{position:absolute;width:56px;height:6px;background:var(--orange)}
.body{position:absolute;font-size:12.5px;line-height:19.3px;color:var(--text)}
.sticker{left:606px;top:643px;width:492px;height:76px;background:var(--red);transform:rotate(-22.8deg);color:#fff;font-size:44px;font-weight:700;display:flex;align-items:center;justify-content:center;letter-spacing:1px}
.services{left:88px;top:888px;width:1024px;height:193px;border:1.5px solid var(--ink);display:flex}
.tile{position:relative;height:100%;background:var(--green);border-left:1.5px solid var(--ink)}
.tile:first-child{background:#fff;border-left:none}
.tile .label{position:absolute;left:0;right:0;font-size:14px;font-weight:600;color:var(--ink);text-align:center;white-space:nowrap}
.tile .tab{position:absolute;left:0;right:0;top:0;height:38px;background:var(--orange);border-bottom:1.5px solid var(--ink);display:flex;align-items:center;justify-content:center}
.tile svg{position:absolute;left:50%;transform:translateX(-50%)}
.arrow{position:absolute;top:1116px;width:31px;height:31px;border-radius:50%;background:var(--orange)}
.promo{left:0;top:1201px;width:1200px;height:212px;background:var(--orange);color:#fff;text-align:center}
.promo h3{position:absolute;left:0;width:1200px;top:32px;font-size:14px;font-weight:700}
.promo p{position:absolute;left:0;width:1200px;top:72px;font-size:12.5px;line-height:19px}
.contact-info{position:absolute;left:88px;font-size:12.5px;line-height:19.3px;color:var(--ink)}
.footer{left:0;top:1961px;width:1200px;height:1315px;background:var(--footer)}
.fcol{position:absolute;top:44px;font-size:10.5px;line-height:15px;color:#444}
.fcol h4{font-size:12.5px;font-weight:700;color:var(--ink);margin-bottom:14px;letter-spacing:.3px}
.copy{position:absolute;left:966px;top:228px;font-size:11px;color:#444}
</style>
</head>
<body>
<div class="page">

  <div class="abs topbar">
    <div class="item" style="left:801px">
      <svg width="13" height="13" viewBox="0 0 24 24" fill="none" stroke="#333" stroke-width="2"><path d="M22 16.9v3a2 2 0 0 1-2.2 2 19.8 19.8 0 0 1-8.6-3.1 19.5 19.5 0 0 1-6-6A19.8 19.8 0 0 1 2.1 4.2 2 2 0 0 1 4.1 2h3a2 2 0 0 1 2 1.7c.1 1 .4 1.9.7 2.8a2 2 0 0 1-.5 2.1L8 9.9a16 16 0 0 0 6 6l1.3-1.3a2 2 0 0 1 2.1-.4c.9.3 1.8.6 2.8.7a2 2 0 0 1 1.7 2z"/></svg>
      +49 (0) 40 88 213 57
    </div>
    <div class="item" style="left:952px">
      <svg width="14" height="12" viewBox="0 0 24 20" fill="none" stroke="#333" stroke-width="2"><rect x="2" y="2" width="20" height="16" rx="2"/><path d="M2 4l10 7 10-7"/></svg>
      INFO@STEINMEISTER.DE
    </div>
  </div>

  <div class="abs header">
    <div class="brand">der Steinmeister</div>
    <svg class="abs" style="left:614px;top:54px" width="28" height="10" viewBox="0 0 28 10">
      <rect x="7" y="0" width="13" height="4" fill="var(--orange)"/>
      <rect x="0" y="5" width="13" height="4" fill="var(--orange)"/>
      <rect x="14" y="5" width="13" height="4" fill="var(--orange)"/>
    </svg>
    <nav class="nav">
      <a style="left:605px">HOME</a>
      <a style="left:698px">ÜBER UNS</a>
      <a style="left:817px">LEISTUNGEN</a>
      <a style="left:956px">SHOP</a>
      <a style="left:1043px">KONTAKT</a>
    </nav>
  </div>

  <section class="abs hero">
    <div class="hero-panel">
      <svg class="abs" style="left:0;top:0" width="519" height="329"><polygon points="0,283 519,309 519,329 0,329" fill="var(--orange-dark)"/></svg>
      <h1>Herzlich willkommen</h1>
      <p>auf unserer Unternehmensseite.<br>Hier finden Sie alle Themen im Bereich der<br>Unternehmensvorstellung, Nachhaltigkeit<br>und Karriere. Unser Produktsortiment<br>finden Sie direkt im Shop.</p>
      <div class="btn" style="left:229px;top:232px;width:131px;height:32px">ZUM SHOP</div>
    </div>
    <div class="hero-photo" role="img" aria-label="Foto der Filiale: rotes Gebäude mit Glasfront und Fahne"></div>
  </section>

  <h2 style="left:88px;top:545px">Über Uns</h2>
  <div class="rule" style="left:88px;top:599px"></div>
  <p class="body" style="left:88px;top:634px;width:478px">Lorem ipsum dolor sit amet, consetetur sadipscing elitr, sed diam nonumy eirmod tempor invidunt ut labore et dolore magna aliquyam erat, sed diam voluptua. At vero eos et accusam et justo duo dolores et ea rebum. Stet clita kasd gubergren, no sea takimata sanctus est Lorem ipsum dolor sit amet. Lorem ipsum dolor sit amet, consetetur sadipscing elitr, sed diam nonumy eirmod tempor invidunt ut labore et dolore magna aliquyam erat, sed diam voluptua. At vero eos et accusam et justo duo dolores et ea rebum. Stet clita kasd gubergren, no sea takimata sanctus est Lorem ipsum dolor sit amet.</p>
  <div class="abs sticker">STEINMEISTER</div>

  <div class="abs services">
    <div class="tile" style="width:194px">
      <div class="abs" role="img" aria-label="Comicfigur mit Zylinder hält einen Ziegelstein" style="left:42px;top:26px;width:110px;height:112px;background:radial-gradient(circle at 50% 45%,#3c4a8a 0%,#1e2430 70%,#fff 71%)"></div>
      <div class="label" style="top:155px">UNSERE LEISTUNGEN</div>
    </div>
    <div class="tile" style="width:167px">
      <div class="tab"><span class="label" style="position:static">GARTEN &amp; TERRASSE</span></div>
      <svg style="top:68px" width="86" height="70" viewBox="0 0 86 70" fill="none" stroke="#111" stroke-width="2.5">
        <circle cx="26" cy="26" r="20"/><path d="M26 28v36M26 40l-9-8M26 36l8-7"/>
        <circle cx="60" cy="34" r="15"/><path d="M60 36v28M60 46l6-6"/><path d="M4 66h80"/>
      </svg>
    </div>
    <div class="tile" style="width:166px">
      <div class="tab"><span class="label" style="position:static">ROH- &amp; HOCHBAU</span></div>
      <svg style="top:62px" width="86" height="80" viewBox="0 0 86 80" fill="none" stroke="#111" stroke-width="2.5">
        <path d="M28 14v64M38 14v64M28 78h10"/><path d="M28 24l10 10M38 34l-10 10M28 44l10 10M38 54l-10 10"/>
        <path d="M4 20h80M4 20l29-14 29 14"/><path d="M76 20v18"/><path d="M73 38h6l-3 5z"/>
      </svg>
    </div>
    <div class="tile" style="width:166px">
      <div class="abs" style="left:0;right:0;top:40px;text-align:center;font-size:78px;font-weight:700;color:#e8003d;line-height:1">?</div>
      <div class="label" style="top:155px">BAUSPEZIALARTIKEL</div>
    </div>
    <div class="tile" style="width:166px">
      <div class="tab"><span class="label" style="position:static">TROCKENBAU</span></div>
      <svg style="top:62px" width="80" height="76" viewBox="0 0 80 76" fill="none" stroke="#111" stroke-width="2.5">
        <rect x="4" y="4" width="72" height="68"/><path d="M40 4v68M4 38h72M14 4v68M22 4v68"/>
        <path d="M14 16h8M14 28h8M14 50h8M14 62h8"/><circle cx="50" cy="14" r="1"/><circle cx="66" cy="14" r="1"/><circle cx="50" cy="62" r="1"/><circle cx="66" cy="62" r="1"/>
      </svg>
    </div>
    <div class="tile" style="width:165px">
      <svg style="top:68px" width="70" height="60" viewBox="0 0 70 60" fill="none" stroke="#111" stroke-width="2.5">
        <path d="M2 18h14M16 12h8v12h-8z"/><path d="M24 8h36v20H24z"/><path d="M42 28l2 20h14l2-20"/><rect x="38" y="48" width="26" height="8"/>
      </svg>
      <div class="label" style="top:152px">HANDWERKZEUGE</div>
    </div>
  </div>

  <div class="arrow" style="left:1040px">
    <svg width="31" height="31" viewBox="0 0 31 31" fill="none" stroke="#111" stroke-width="2.2"><path d="M18 9l-6 6.5 6 6.5"/></svg>
  </div>
  <div class="arrow" style="left:1081px">
    <svg width="31" height="31" viewBox="0 0 31 31" fill="none" stroke="#111" stroke-width="2.2"><path d="M13 9l6 6.5-6 6.5"/></svg>
  </div>

  <section class="abs promo">
    <h3>100.000 Produkte auf einen Klick</h3>
    <p>Als führender Baustoffhandel von Nordbau Gruppe bietet Kellmann Baustoffe Profi-Handwerkern an über 220 Standorten alles aus einer Hand – jetzt auch in unserem Onlineshop.<br>Ob Hochbau, Rohbau, Tiefbau, im Bereich Fliese und alternative Bodenbeläge sowie beim Trockenbau, Dach, Fassade oder Gartenbau – hier findest du alles bequem online.</p>
    <div class="btn" style="left:535px;top:139px;width:130px;height:32px">ZUM SHOP</div>
  </section>

  <div class="contact-info" style="top:1592px">
    <b>Fragen zum Onlineshop:</b><br>So erreichst du unseren technischen Support:<br><br>+49 69 447210-300<br><br><b>Erreichbarkeit</b><br>Mo-Do:<br>8:00 bis 17:00 Uhr<br>Fr:<br>8:00 bis 16:00 Uhr
  </div>
  <div class="btn" style="left:88px;top:1801px;width:213px;height:32px">ZUM KONTAKTFORMULAR</div>

  <h2 style="left:624px;top:1491px">Kontakt</h2>
  <div class="rule" style="left:624px;top:1544px"></div>
  <div class="body" style="left:624px;top:1580px;width:488px">
    <p>Lorem ipsum dolor sit amet, consetetur sadipscing elitr, sed diam nonumy eirmod tempor invidunt ut labore et dolore magna aliquyam erat, sed diam voluptua. At vero eos et accusam et justo duo dolores et ea rebum. Stet clita kasd gubergren, no sea takimata sanctus est Lorem ipsum dolor sit amet. Lorem ipsum dolor sit amet, consetetur sadipscing elitr, sed diam nonumy eirmod tempor invidunt ut labore et dolore magna aliquyam erat, sed diam voluptua. At vero eos et accusam et justo duo dolores et ea rebum. Stet clita kasd gubergren, no sea takimata sanctus est Lorem ipsum dolor sit amet.</p>
    <p style="margin-top:19px">Lorem ipsum dolor sit amet, consetetur sadipscing elitr, sed diam nonumy eirmod tempor invidunt ut labore et dolore magna aliquyam erat, sed diam voluptua. At vero eos et accusam et justo duo dolores et ea rebum. Stet clita kasd gubergren, no sea takimata sanctus est Lorem ipsum dolor sit amet.</p>
  </div>

  <footer class="abs footer">
    <div class="fcol" style="left:88px"><h4>HILFE &amp; KONTAKT</h4>FAQ<br>Kontakt<br>Lieferung &amp; Versand<br>E-Procurement / EDI Lösungen</div>
    <div class="fcol" style="left:346px"><h4>UNTERNEHMEN</h4>Über uns<br>Karriere<br>Presse<br>Nachhaltigkeit</div>
    <div class="fcol" style="left:553px"><h4>RECHTLICHES</h4>Über uns<br>Karriere<br>Presse<br>Nachhaltigkeit</div>
    <div class="fcol" style="left:744px"><h4>RECHTLICHES</h4>AGB<br>Impressum<br>Datenschutz<br>Hinweisgebersystem<br>Menschenrechtserklärung<br>Sitemap<br>Leistungserklärungen</div>
    <div class="fcol" style="left:979px"><h4>ZAHLUNGSARTEN</h4></div>
    <div class="copy">© 2025 derSteinmeister</div>
  </footer>

</div>
</body>
</html>
```